THIS IS A LATIN MUSICAL CD BUT IN ENGLISH THE TITLE WOULD BE “BENEATH THE QUIET RAIN" JUST THAT YOU K

DIGIPACK CD COVER

THIS IS THE INFO NEEDED ON THE FRONT COVER

CD TITLE "BAJO LA LLUVIA SERENA"
ARTIST: ELÍAS MORO

I WOULD NEED A GREAT DESIGN TO WIN A PREMIO SOLAR FOR THIS MUSICAL PROJECT. I WANT A DESIGN THAT MAY CONTAIN TERMS AS HOPE, LOVE , FREEDOM , SALVATION.

I WILL ATTACH THE PRINCIPAL SONG CALL “BENEATH THE QUIET RAIN" MAYBE YOU CAN FIND INSPIRATION AND A PICTURE OF MY GUITAR.

THIS IS THE INFO NEEDED FOR THE BACK COVER , INSIDE COVERS TOO

SONGS:
1 BAJO LA LLUVIA SERENA
2 TOCASTE MI VIDA
3 ME ENAMORÉ DE TÍ
4 SANTO ESPÍRITU DIVINO
5 TU MIRAR
6 MAJESTAD
7 REY DE LOS CIELOS
8 TU AMOR ME INUNDÓ
9 TOCASTE MI VIDA (DISCO)
10 VIDA TU ME DAS
Updates

Hi People i will like to say thanks for be part of this project, the truth is that I do not like to be on the cover of the disc playing my guitar even though I have pictures playing in HD, I would like more a kind of art that reflects peace, hope, salvation , also could be natural landscapes that reflect the title of the album or situations in the real life where the phrase is reflected *beneath the quiet rain*(Album Title) ,or maybe a little child with headphones and looking the sky its just a couple of ideas you can consider, the primary focus is what happens when we hear the name of God , referent to the letters i would like to see fonts more modern . Cheers!!!!! Added Tuesday, June 9, 2015

Project Deadline Extended Reason: im currently working with all of your designs on small details. Once this is done i will have a final decision.Thank you for being part of this project Sincerely,Elias Moro Added Tuesday, June 16, 2015

Target Market(s)

all people who believe in God and not

Industry/Entity Type

Religious

Font styles to use
Serif
Sans Serif
Decorative
Script

Requirements
Must have
• original design , i will like to say thanks for be part of this project, ,I would like more a kind of art that reflects peace, hope, salvation , also could be natural landscapes that reflect the title of the album or situations in the real life where the phrase is reflected BENEATH THE QUIET RAIN (GOD) , the primary focus is what happens when we hear the name of God , the market is for people who believe in God , referent to the letters i would like to see fonts more modern, however I will be here to hope see ALL your talent friends god bless you cheers
Nice to have
• natural landscapes with people that represent the concept of the album or actual scene of daily living, also modern fonts,
Should not have
• the moon, the skeleton , dead signals , dark things, satan draws, the chains and the handaxes,etc. reflect the opposite way that i want to proyect in this music i want to proyect through my music is hope, salvation, peace, and the principal objective that is WHAT HAPPEN WHEN I HEAR THE NAME OF GOD when we live in difficult situations

```html
<!DOCTYPE html>
<html lang="es">
<head>
<meta charset="utf-8">
<title>Bajo la Lluvia Serena — Elías Moro</title>
<link rel="stylesheet" href="https://fonts.googleapis.com/css2?family=Megrim&display=swap">
<style>
  :root {
    --backdrop: #8f8f8f;
    --sleeve: #f4f4f2;
    --sky-top: #9ea3a0;
    --sky-mid: #c3c7bd;
    --haze: #dcdcc8;
    --field-light: #6f8a4a;
    --field-deep: #3c5532;
    --ink: #ffffff;
  }
  * { box-sizing: border-box; margin: 0; padding: 0; }
  html, body {
    width: 1200px;
    height: 923px;
    overflow: hidden;
    background: var(--backdrop);
  }
  .canvas {
    width: 1200px;
    height: 923px;
    display: flex;
    align-items: center;
    justify-content: center;
  }
  .cover {
    width: 760px;
    height: 760px;
    background: var(--sleeve);
    padding: 38px;
  }
  .cover-art {
    position: relative;
    width: 100%;
    height: 100%;
    overflow: hidden;
  }
  .cover-photo {
    position: absolute;
    inset: 0;
    background:
      radial-gradient(ellipse 60% 30% at 78% 18%, var(--haze) 0%, rgba(220,220,200,0) 70%),
      linear-gradient(180deg,
        var(--sky-top) 0%,
        var(--sky-mid) 38%,
        #a9ae98 52%,
        var(--field-light) 64%,
        var(--field-deep) 100%);
  }
  .cover-type {
    position: absolute;
    inset: 0;
    font-family: "Megrim", sans-serif;
    color: var(--ink);
    text-align: center;
    font-size: 44px;
    font-weight: 400;
    letter-spacing: 0.32em;
  }
  .album-title { font-size: inherit; font-weight: inherit; }
  .title-line,
  .artist-name {
    position: absolute;
    left: 0;
    right: 0;
    line-height: 1;
    padding-left: 0.32em;
    transform: translateY(-50%);
    white-space: nowrap;
  }
  .title-line--lead { top: 25%; }
  .title-line--middle { top: 44%; }
  .title-line--last { top: 63%; }
  .artist-name { top: 90%; }
  .rule {
    position: absolute;
    height: 3px;
    background: var(--ink);
  }
  .rule--top { top: 20.5%; width: 30px; }
  .rule--top-left { left: 18%; }
  .rule--top-right { right: 18%; }
  .rule--bottom { top: 77%; width: 56px; }
  .rule--bottom-left { left: 28%; }
  .rule--bottom-right { right: 28%; }
</style>
</head>
<body>
  <main class="canvas">
    <section class="cover">
      <div class="cover-art">
        <div class="cover-photo" role="img" aria-label="Photograph of a person leaping into the air above a grassy hilltop under a hazy, sunlit sky"></div>
        <div class="cover-type">
          <span class="rule rule--top rule--top-left"></span>
          <span class="rule rule--top rule--top-right"></span>
          <h1 class="album-title">
            <span class="title-line title-line--lead">BAJO</span>
            <span class="title-line title-line--middle">LA LLUVIA</span>
            <span class="title-line title-line--last">SERENA</span>
          </h1>
          <span class="rule rule--bottom rule--bottom-left"></span>
          <span class="rule rule--bottom rule--bottom-right"></span>
          <p class="artist-name">ELÍAS MORO</p>
        </div>
      </div>
    </section>
  </main>
</body>
</html>
```